Kneadwell Bodycare Studio

We are a Massage Therapy business based in Invercargill, New Zealand. We specialise in Sports and deep tissue massage but also provide relaxation and aromatherapy massage. We would like to see designs that use the the logo.
The final design should promote health and fitness.
Updates

Hi I am getting feedback that my business card picture is poor quality. I got this picture from brightpress under massage. So if you google this image a better quality picture should come up,. If not hope to upload a better image by tomorow, thanks.

Target Market(s)

Sports, people with pain and injuries

Industry/Entity Type

Massage

Requirements
Must have
• Logo, muscle body that is used on the business card, also a poster that matches my business card
Nice to have
• Picture of muscle man, shown on my business card
Should not have
• Not a picture of a real person

```html
<!DOCTYPE html>
<html lang="en">
<head>
<meta charset="utf-8">
<title>Kneadwell Bodycare Studio – Poster</title>
<link rel="stylesheet" href="https://fonts.googleapis.com/css2?family=Archivo+Black&family=Cinzel:wght@400;500&family=Arimo:wght@700&display=swap">
<style>
  :root {
    --sky: #86c5ef;
    --sky-ring: #2f86cc;
    --deep: #0e3f9c;
    --deep-light: #1f5fc2;
    --footer: #0c5db4;
    --footer-line: #7cc4f2;
    --accent: #f4e23a;
    --white: #ffffff;
    --ink: #0a0a0a;
    --teal: #35c4c6;
    --skin: #b97a55;
    --skin-dark: #6e3f24;
    --divider: #8fd0f5;
  }
  * { margin: 0; padding: 0; box-sizing: border-box; }
  html, body { width: 900px; height: 1200px; overflow: hidden; background: #ffffff; }
  .poster { position: relative; width: 900px; height: 1200px; overflow: hidden; background: var(--sky); }
  .poster-shapes { position: absolute; inset: 0; }
  .headline {
    position: absolute; right: 30px; top: 78px; text-align: right;
    font-family: "Archivo Black", "Arial Black", sans-serif; color: var(--ink); line-height: 1;
  }
  .headline .lead { display: block; font-size: 56px; margin-right: 150px; }
  .headline .key { display: block; font-size: 104px; margin-top: 2px; }
  .brand-name {
    position: absolute; left: 0; right: 0; top: 398px; text-align: center;
    font-family: "Cinzel", "Trajan Pro", serif; font-weight: 400; font-size: 50px;
    color: var(--ink); letter-spacing: 0.5px;
  }
  .services {
    position: absolute; right: 434px; top: 548px; text-align: right; list-style: none;
    font-family: "Cinzel", serif; font-size: 42px; line-height: 66.5px;
  }
  .services li { color: var(--white); }
  .services li.highlight { color: var(--accent); }
  .prices {
    position: absolute; left: 530px; top: 718px;
    font-family: "Cinzel", serif; font-size: 33px; line-height: 54px; color: var(--white);
  }
  .prices .prices-title { color: var(--accent); }
  .contact {
    position: absolute; right: 48px; top: 1038px; text-align: right;
    font-family: "Arimo", Arial, sans-serif; font-weight: 700; font-size: 28px;
    line-height: 36px; color: var(--accent);
  }
</style>
</head>
<body>
<main class="poster">
  <svg class="poster-shapes" width="900" height="1200" viewBox="0 0 900 1200" aria-hidden="false">
    <defs>
      <linearGradient id="massage-photo-tone" x1="0" y1="0" x2="1" y2="1">
        <stop offset="0" stop-color="#d6a07c"/>
        <stop offset="0.55" stop-color="var(--skin)"/>
        <stop offset="1" stop-color="var(--skin-dark)"/>
      </linearGradient>
      <linearGradient id="spa-photo-tone" x1="0" y1="0" x2="0" y2="1">
        <stop offset="0" stop-color="var(--deep-light)"/>
        <stop offset="0.6" stop-color="var(--deep)"/>
        <stop offset="1" stop-color="#0a3286"/>
      </linearGradient>
    </defs>

    <!-- spa stones and candles photo zone -->
    <rect x="0" y="496" width="900" height="560" fill="url(#spa-photo-tone)" role="img" aria-label="Photo of stacked massage stones, bamboo and candles in blue tones"/>

    <!-- light band under header -->
    <path d="M0 270 L900 300 L900 498 L0 520 Z" fill="var(--sky)"/>

    <!-- massage photo top left -->
    <path d="M0 0 L262 0 C268 150 380 290 560 328 L0 282 Z" fill="url(#massage-photo-tone)" role="img" aria-label="Photo of hands massaging a person's back"/>

    <!-- header circle -->
    <path d="M258 -10 C262 190 420 332 600 334 C720 334 830 300 910 246 L910 -10 Z" fill="var(--sky)" stroke="var(--sky-ring)" stroke-width="14"/>
    <path d="M720 322 C800 305 860 282 900 262 L900 300 C860 312 800 322 720 322 Z" fill="var(--sky-ring)"/>

    <!-- brand mark: plain circle -->
    <circle cx="640" cy="332" r="47" fill="var(--white)"/>
    <circle cx="640" cy="332" r="40" fill="var(--teal)"/>

    <!-- divider between services and prices -->
    <rect x="502" y="600" width="6" height="343" fill="var(--divider)"/>

    <!-- footer band -->
    <path d="M0 1044 C300 1040 700 1010 900 962 L900 1200 L0 1200 Z" fill="var(--footer)"/>
    <path d="M0 1044 C300 1040 700 1010 900 962" fill="none" stroke="var(--footer-line)" stroke-width="4"/>
  </svg>

  <h1 class="headline"><span class="lead">Are you in</span><span class="key">PAIN?</span></h1>

  <h2 class="brand-name">Kneadwell Bodycare Studio</h2>

  <ul class="services">
    <li>Deep Tissue</li>
    <li class="highlight">Sports Massage</li>
    <li>Relaxation</li>
    <li class="highlight">Aromatherapy</li>
    <li>Hot Stones</li>
  </ul>

  <div class="prices">
    <p class="prices-title">Prices</p>
    <p>30minutes $40</p>
    <p>60minutes $60</p>
    <p>90 minutes $80</p>
  </div>

  <address class="contact" style="font-style:normal">
    <p>0270418826</p>
    <p>18 Larch Lane, Invercargill 9810</p>
    <p>Maren Holt Bachelor Therapeutic</p>
    <p>&amp; Sports massage</p>
  </address>
</main>
</body>
</html>
```